Redesign of the UI of a customer service platform

To improve the user experience of our customers, we need a new design for our agent interface of our customer service platform (quillvane.com).
The focus will be on the dashboard and the inbox screens (see attached) along with the common UI elements (Buttons, menu, fonts, forms...)
We want a simple and distinctive design

Target Market(s)

Worldwide

Industry/Entity Type

It Service

Number of Pages Required

3 page

Font styles to use
Sans Serif

Requirements
Must have
• New Onboarding page: this is a new page that is shown to user the first time they login to the platform. This will replace the current onboarding screen (setup SMS, Setup widget...etc)
• Dashboard page: to access important information and activate services (see screenshot from current site)
• Inbox page: to manage all the interactions with customers. (see screenshot from current site)
• UI elements (buttons, menus, forms, tables, fonts, color palette)

```html
<!DOCTYPE html>
<html lang="en">
<head>
<meta charset="utf-8">
<title>quillvane – Get Started</title>
<link href="https://fonts.googleapis.com/css2?family=Ubuntu:wght@300;400;500&display=swap" rel="stylesheet">
<style>
:root{
  --accent:#f05228;
  --green:#3cae2c;
  --red:#e3161c;
  --yellow:#f9b800;
  --bg-gray:#f2f2f2;
  --white:#ffffff;
  --line:#e3e3e3;
  --icon:#a8a8a8;
  --text:#333333;
  --muted:#8a8a8a;
}
*{box-sizing:border-box;margin:0;padding:0}
html,body{width:1200px;height:1172px;overflow:hidden;background:var(--white);font-family:"Ubuntu",sans-serif;color:var(--text)}
.canvas{position:relative;width:1200px;height:1172px}

/* top bar */
.topbar{position:absolute;left:0;top:0;width:1200px;height:83px;background:var(--white);display:flex}
.brand{width:83px;height:83px;background:var(--accent);display:flex;align-items:center;justify-content:center;color:var(--white);font-size:13px;font-weight:400}
.nav{display:flex}
.nav-item{position:relative;width:84px;height:83px;border-right:1px solid #efefef;display:flex;flex-direction:column;align-items:center;padding-top:16px;color:var(--muted);font-size:13px;font-weight:300}
.nav-item svg{width:28px;height:28px;fill:var(--icon);margin-bottom:10px}
.count{position:absolute;top:17px;left:50px;width:23px;height:23px;border-radius:50%;color:var(--white);font-size:11px;font-weight:500;display:flex;align-items:center;justify-content:center}
.count.red{background:var(--red)}
.count.yellow{background:var(--yellow)}
.user{position:absolute;right:14px;top:14px;width:54px;height:54px;border-radius:50%;background:linear-gradient(#d8d6d2,#eeeeec)}
.user::after{content:"";position:absolute;left:-2px;top:0;width:14px;height:14px;border-radius:50%;background:var(--green)}

/* onboarding */
.onboarding{position:absolute;left:0;top:83px;width:1200px;height:679px;background:var(--bg-gray)}
.heading{position:absolute;left:0;width:100%;text-align:center;font-weight:400}
.onboarding .title{top:30px;font-size:27px}
.video{position:absolute;left:344px;top:94px;width:513px;height:299px;background:radial-gradient(circle at 70% 25%,#f3e0b5 0%,#d89c62 30%,#8a5a3e 65%,#463730 100%)}
.play{position:absolute;left:222px;top:115px;width:70px;height:70px;border-radius:50%;background:rgba(255,255,255,.85);display:flex;align-items:center;justify-content:center}
.play svg{width:22px;height:22px;fill:var(--accent);margin-left:4px}
.controls{position:absolute;left:344px;top:408px;width:513px;height:14px;display:flex;align-items:center;font-size:11px;color:#b0b0b0;font-weight:300}
.controls svg{width:8px;height:9px;fill:#b0b0b0;margin-right:10px}
.track{position:absolute;left:49px;right:0;height:3px;background:#dcdcdc}
.track span{display:block;width:233px;height:3px;background:var(--accent)}
.onboarding .subtitle{top:462px;font-size:20px}
.addons{position:absolute;left:183px;top:507px;display:flex;gap:19px}
.addon{position:relative;width:152px;height:153px;background:var(--white);border:1px solid var(--line);display:flex;flex-direction:column;align-items:center;padding-top:19px}
.addon .ring{width:65px;height:65px;border-radius:50%;border:1px solid var(--line);display:flex;align-items:center;justify-content:center}
.addon .ring svg{width:28px;height:28px;fill:var(--icon)}
.addon h3{font-size:17px;font-weight:400;margin-top:14px}
.addon a{font-size:11px;color:var(--accent);text-decoration:none;margin-top:7px;letter-spacing:.3px}
.addon .check{position:absolute;left:10px;top:10px;width:20px;height:20px}

/* plan */
.plan .title{top:805px;font-size:22px}
.badge-free{display:inline-block;vertical-align:5px;margin-left:6px;background:var(--red);color:var(--white);font-size:10px;font-weight:500;padding:3px 6px;border-radius:2px}
.plan .note{top:836px;font-size:14px;color:var(--muted);font-weight:300}
.limits{position:absolute;left:279px;top:932px;display:flex;gap:29px}
.limit{position:relative;width:196px;height:130px;border:1px solid var(--line);text-align:center;padding-top:56px}
.limit .disc{position:absolute;left:65px;top:-32px;width:65px;height:65px;border-radius:50%;background:#e6e6e6;display:flex;align-items:center;justify-content:center}
.limit .disc svg{width:32px;height:32px;fill:#9a9a9a}
.limit .used{position:absolute;left:113px;top:-46px;width:36px;height:36px;border-radius:50%;background:var(--accent);color:var(--white);font-size:11px;display:flex;align-items:center;justify-content:center}
.limit h4{font-size:16px;font-weight:400}
.limit p{font-size:12px;color:var(--muted);margin-top:4px}
.buy{position:absolute;left:558px;top:1100px;width:84px;height:27px;background:var(--green);color:var(--white);font-size:12px;font-weight:500;border:none;display:flex;align-items:center;justify-content:center;font-family:inherit}
</style>
</head>
<body>
<div class="canvas">
  <header class="topbar">
    <div class="brand">quillvane</div>
    <nav class="nav">
      <div class="nav-item"><svg viewBox="0 0 28 28"><path d="M3 15h6l2 3h6l2-3h6v9H3z"/><path d="M13 3h2v7h3l-4 4-4-4h3z"/></svg>Inbox<span class="count red">4</span></div>
      <div class="nav-item"><svg viewBox="0 0 28 28"><path d="M5 3h16v12l-3 3v-13H7v18h9v2H5z"/><path d="M9 9h8v2H9zM9 13h8v2H9zM9 17h5v2H9z"/></svg>Tasks<span class="count yellow">1</span></div>
      <div class="nav-item"><svg viewBox="0 0 28 28"><circle cx="14" cy="9" r="5"/><path d="M4 25c0-6 4-10 10-10s10 4 10 10z"/></svg>Customers</div>
      <div class="nav-item"><svg viewBox="0 0 28 28"><path d="M2 4l24 10L2 24l3-10zM6 13l-2-6 16 7zM6 15l14 0-16 7z"/></svg>Campaigns</div>
      <div class="nav-item"><svg viewBox="0 0 28 28"><path d="M13 2h2v3c3 0 5 2 5 4h-2c0-1-1-2-4-2s-4 1-4 3 2 2 4 3c3 1 6 2 6 5 0 3-2 5-5 5v3h-2v-3c-3 0-6-2-6-5h2c0 2 2 3 5 3s4-1 4-3-2-2-4-3c-3-1-6-2-6-5 0-3 2-4 5-5z"/></svg>Payments</div>
      <div class="nav-item"><svg viewBox="0 0 28 28"><path d="M4 3h2v22H4zM10 8h2v17h-2zM16 3h2v22h-2zM22 11h2v14h-2z"/></svg>Reports</div>
      <div class="nav-item"><svg viewBox="0 0 28 28"><path d="M12 2h4l1 4 3 1 3-2 3 3-2 3 1 3 4 1v4l-4 1-1 3 2 3-3 3-3-2-3 1-1 4h-4l-1-4-3-1-3 2-3-3 2-3-1-3-4-1v-4l4-1 1-3-2-3 3-3 3 2 3-1zM14 10a4 4 0 100 8 4 4 0 000-8z"/></svg>Settings</div>
    </nav>
    <div class="user" role="img" aria-label="Agent profile photo"></div>
  </header>

  <section class="onboarding">
    <h1 class="heading title">Get Started</h1>
    <div class="video" role="img" aria-label="Intro video still: colleagues planning at a sunlit desk">
      <div class="play"><svg viewBox="0 0 20 22"><path d="M0 0l20 11L0 22z"/></svg></div>
    </div>
    <div class="controls">
      <svg viewBox="0 0 8 9"><path d="M0 0l8 4.5L0 9z"/></svg>0:00
      <div class="track"><span></span></div>
    </div>
    <h2 class="heading subtitle">Select Your Add-ons</h2>
    <div class="addons">
      <div class="addon">
        <div class="ring"><svg viewBox="0 0 28 28"><path d="M2 5h24v15H2zM4 7v11h20V7zM11 20h6l1 3h3v2H7v-2h3z"/></svg></div>
        <h3>Campaigns</h3><a href="#">WATCH VIDEO</a>
      </div>
      <div class="addon">
        <div class="ring"></div>
        <h3>Chatline</h3><a href="#">WATCH VIDEO</a>
      </div>
      <div class="addon">
        <svg class="check" viewBox="0 0 20 20"><circle cx="10" cy="10" r="10" fill="#3cae2c"/><path d="M5 10l3 3 7-7" stroke="#fff" stroke-width="2.4" fill="none"/></svg>
        <div class="ring"><svg viewBox="0 0 28 28"><path d="M14 3C7 3 2 8 2 13c0 3 2 6 5 8l-1 5 6-4h2c7 0 12-4 12-9S21 3 14 3zM9 10h10v1.6H9zm0 3.5h10v1.6H9z"/></svg></div>
        <h3>SMS</h3><a href="#">WATCH VIDEO</a>
      </div>
      <div class="addon">
        <div class="ring"></div>
        <h3>Pingrelay</h3><a href="#">WATCH VIDEO</a>
      </div>
      <div class="addon">
        <div class="ring"><svg viewBox="0 0 28 28"><path d="M13 2h2v3c3 0 5 2 5 4h-3c0-1-1-1.5-3-1.5s-3 .8-3 2c0 1.3 1.5 1.7 4 2.5 3 1 5 2 5 5 0 2.5-2 4.5-5 5v3h-2v-3c-3-.5-6-2-6-5h3c0 1.5 1.5 2.5 4 2.5s3-1 3-2.2c0-1.3-1.5-1.8-4-2.6-3-1-5-2-5-4.7 0-2.5 2-4.3 5-4.7z"/></svg></div>
        <h3>Payment</h3><a href="#">WATCH VIDEO</a>
      </div>
    </div>
  </section>

  <section class="plan">
    <h2 class="heading title">Plan<span class="badge-free">FREE</span></h2>
    <p class="heading note">Your trial period ends in 14 days</p>
    <div class="limits">
      <div class="limit">
        <div class="disc"><svg viewBox="0 0 32 32"><circle cx="16" cy="10" r="4"/><circle cx="8" cy="12" r="3"/><circle cx="24" cy="12" r="3"/><path d="M9 26c0-5 3-9 7-9s7 4 7 9zM2 24c0-4 2-7 6-7 1 0 2 .3 2 .5-2 2-3 4-3 6.5zM30 24c0-4-2-7-6-7-1 0-2 .3-2 .5 2 2 3 4 3 6.5z"/></svg></div>
        <span class="used">1/3</span>
        <h4>Agents</h4><p>Up to 3</p>
      </div>
      <div class="limit">
        <div class="disc"><svg viewBox="0 0 32 32"><path d="M12 6h8v3h7v7H5V9h7zm2 2v1h4V8zM5 18h10v2h2v-2h10v8H5z"/></svg></div>
        <span class="used">1/3</span>
        <h4>Departments</h4><p>Up to 3</p>
      </div>
      <div class="limit">
        <div class="disc"><svg viewBox="0 0 32 32"><path d="M8 4l5 5-3 3c1 3 4 7 8 9l3-3 5 5-4 4C13 26 6 19 4 8z"/></svg></div>
        <span class="used">1/3</span>
        <h4>Phones</h4><p>Up to 1</p>
      </div>
    </div>
    <button class="buy">BUY NOW</button>
  </section>
</div>
</body>
</html>
```